Amber Hollow Cafe Business Card

We need a business card design for a new European Cafe. Main menu will be coffee and deserts.

Industry/Entity Type

Business

Requirements
Must have
• Logo - 1 of the attached versions
Address - TBA (you can use 123 Fake St Unit 1 for now)
Phone - TBA (you can use 555-555-5555 for now)

```html
<!DOCTYPE html>
<html lang="en">
<head>
<meta charset="utf-8">
<title>Amber Hollow Cafe Business Card</title>
<link rel="stylesheet" href="https://fonts.googleapis.com/css2?family=Nunito+Sans:wght@400;600;800&display=swap">
<style>
  :root {
    --backdrop: #e4e4e4;
    --card: #ffffff;
    --brand-red: #b52025;
    --ink: #1c1c1c;
    --decor-tint: #f2d6ca;
  }
  html, body {
    margin: 0;
    padding: 0;
    width: 1200px;
    height: 900px;
    overflow: hidden;
    background: var(--backdrop);
    font-family: "Nunito Sans", "Avenir", sans-serif;
  }
  .business-card {
    position: absolute;
    left: 64px;
    top: 100px;
    width: 1063px;
    height: 615px;
    background: var(--card);
    overflow: hidden;
  }
  .decor-mark {
    position: absolute;
    left: 640px;
    top: 40px;
    width: 520px;
    height: 620px;
  }
  .brand {
    position: absolute;
    left: 56px;
    top: 58px;
    display: flex;
    align-items: center;
    gap: 18px;
  }
  .brand-square {
    width: 100px;
    height: 100px;
    background: var(--brand-red);
    border-radius: 4px;
  }
  .brand-name {
    margin: 0;
    font-size: 40px;
    font-weight: 600;
    color: var(--brand-red);
    line-height: 1;
    letter-spacing: 0.2px;
  }
  .person {
    position: absolute;
    left: 55px;
    top: 302px;
  }
  .person-name {
    margin: 0;
    font-size: 28px;
    font-weight: 800;
    color: var(--brand-red);
    line-height: 1.1;
    letter-spacing: 0.6px;
  }
  .person-title {
    margin: 0;
    font-size: 21px;
    font-weight: 400;
    color: var(--brand-red);
    letter-spacing: 0.6px;
  }
  .contact {
    position: absolute;
    left: 55px;
    top: 410px;
    display: grid;
    grid-template-columns: 124px auto;
    row-gap: 0;
    margin: 0;
    font-size: 24px;
    line-height: 32px;
    letter-spacing: 0.3px;
  }
  .contact dt {
    color: var(--brand-red);
    font-weight: 400;
  }
  .contact dd {
    margin: 0;
    color: var(--ink);
  }
</style>
</head>
<body>
  <main class="business-card">
    <svg class="decor-mark" viewBox="0 0 520 620" role="img" aria-label="Faint brand decoration area">
      <circle cx="300" cy="330" r="240" fill="var(--decor-tint)" opacity="0.55"/>
    </svg>

    <header class="brand">
      <div class="brand-square" aria-hidden="true"></div>
      <h1 class="brand-name">Amber Hollow Cafe</h1>
    </header>

    <section class="person">
      <p class="person-name">Name</p>
      <p class="person-title">Designation</p>
    </section>

    <dl class="contact">
      <dt>Phone</dt><dd>555-555-5555</dd>
      <dt>Email</dt><dd>hello@amberhollow.cafe</dd>
      <dt>Address</dt><dd>123 Fake St<br>Unit 1</dd>
    </dl>
  </main>
</body>
</html>
```